Premium Juice and Wine Bottle Label

We require a premium label design for a Burgundy style wine bottle - the design should reflect pure and organic theme, with a reference to New Zealand blueberries. The winning design will look high-end, simple but sophisticated. Our logo is attached, refer :

https://www.rvcellar.co.nz and https://www.halopu.co.nz/wines/details/coming-soon-showcase/2018

for inspiration.

Target Market(s)

High-end retail grocery stores, wine shops, bars.

Requirements
Must have
• Label should leave enough space for barcode and nutrients/ingredients etc. Reference to New Zealand, natural-beverage, be very high-end in design. Refer links in project description for inspiration. Refer to attached logo, which must be used - feel free to change colour in order to obtain the best high-class design.
Nice to have
• N/A.
Should not have
• Cartoons or pictures of berries.

```html
<!DOCTYPE html>
<html lang="en">
<head>
<meta charset="utf-8">
<title>Marlow Lane – Label Concepts</title>
<link rel="stylesheet" href="https://fonts.googleapis.com/css2?family=Josefin+Sans:wght@600;700&family=Montserrat:wght@800&display=swap">
<style>
  :root {
    --backdrop: #ece8e2;
    --ink: #111111;
    --cream: #f5efe5;
    --cream-warm: #f8f1e8;
    --silver-paper: #ecebe8;
    --gold: #b08a3e;
    --gold-light: #f1d98a;
    --gold-dark: #9c7421;
    --copper: #a87a5a;
    --copper-light: #efc9a6;
    --copper-dark: #8f6244;
    --copper-line: #c29a6c;
    --stitch: #f6e7d8;
    --wine-red: #b8323e;
    --text-font: "Josefin Sans", sans-serif;
    --caption-font: "Montserrat", sans-serif;
  }
  * { margin: 0; padding: 0; box-sizing: border-box; }
  html, body { width: 1200px; height: 825px; overflow: hidden; background: var(--backdrop); }
  .concept-board {
    width: 1200px; height: 825px;
    display: flex; justify-content: space-around; align-items: flex-start;
    padding: 130px 20px 0;
  }
  .concept {
    width: 220px;
    display: flex; flex-direction: column; align-items: center;
  }
  .neck-tag-slot {
    height: 110px; width: 100%;
    display: flex; justify-content: center; align-items: flex-end;
  }
  .body-label { margin-top: 150px; display: block; }
  .concept-caption {
    margin-top: 70px;
    font-family: var(--caption-font);
    font-weight: 800; font-size: 30px; color: var(--ink);
    letter-spacing: 0.5px;
  }
  .vintage { font-family: var(--text-font); font-weight: 700; fill: var(--ink); }
  .brand-name { font-family: var(--text-font); font-weight: 600; fill: var(--gold); }
  .origin { font-family: var(--text-font); font-weight: 700; font-size: 8px; letter-spacing: 0.3px; }
  .origin--dark { fill: #2a2a2a; }
  .origin--red { fill: var(--wine-red); }
</style>
</head>
<body>
<svg width="0" height="0" style="position:absolute" aria-hidden="true">
  <defs>
    <linearGradient id="gold-foil" x1="0" x2="1" y1="0" y2="0">
      <stop offset="0" stop-color="var(--gold-dark)"/>
      <stop offset="0.5" stop-color="var(--gold-light)"/>
      <stop offset="1" stop-color="var(--gold-dark)"/>
    </linearGradient>
    <linearGradient id="copper-foil" x1="0" x2="1" y1="0" y2="0">
      <stop offset="0" stop-color="var(--copper-dark)"/>
      <stop offset="0.5" stop-color="var(--copper-light)"/>
      <stop offset="1" stop-color="var(--copper-dark)"/>
    </linearGradient>
    <linearGradient id="kraft-paper" x1="0" x2="1" y1="0" y2="0">
      <stop offset="0" stop-color="#b88a69"/>
      <stop offset="0.5" stop-color="#dcb596"/>
      <stop offset="1" stop-color="#b48565"/>
    </linearGradient>
    <linearGradient id="brushed-paper" x1="0" x2="1" y1="0" y2="1">
      <stop offset="0" stop-color="#f1f0ed"/>
      <stop offset="1" stop-color="#e4e2de"/>
    </linearGradient>
  </defs>
</svg>

<main class="concept-board">

  <section class="concept concept--one">
    <div class="neck-tag-slot">
      <svg class="neck-tag" width="72" height="80" viewBox="0 0 72 80">
        <path d="M0 0 H72 V64 L36 78 L0 64 Z" fill="url(#gold-foil)"/>
        <text class="vintage" x="36" y="44" text-anchor="middle" font-size="17">2020</text>
      </svg>
    </div>
    <svg class="body-label" width="200" height="180" viewBox="0 0 200 180">
      <rect width="200" height="180" fill="var(--cream)"/>
      <rect x="13" y="13" width="174" height="154" fill="none" stroke="var(--gold)" stroke-width="1"/>
      <text class="brand-name" x="100" y="40" text-anchor="middle" font-size="18"><tspan x="100">Marlow</tspan><tspan x="100" dy="19">Lane</tspan></text>
      <text class="origin origin--dark" x="100" y="161" text-anchor="middle">•• NEW ZEALAND ••</text>
    </svg>
    <p class="concept-caption">DESIGN 1</p>
  </section>

  <section class="concept concept--two">
    <div class="neck-tag-slot"></div>
    <svg class="body-label" width="200" height="180" viewBox="0 0 200 180">
      <rect width="200" height="180" fill="var(--cream-warm)"/>
      <path d="M22 10 H178 A12 12 0 0 0 190 22 V158 A12 12 0 0 0 178 170 H22 A12 12 0 0 0 10 158 V22 A12 12 0 0 0 22 10 Z" fill="none" stroke="var(--copper-line)" stroke-width="1.2"/>
      <text class="brand-name" x="100" y="36" text-anchor="middle" font-size="18"><tspan x="100">Marlow</tspan><tspan x="100" dy="19">Lane</tspan></text>
      <text class="origin origin--red" x="100" y="163" text-anchor="middle">— •• — NEW ZEALAND — •• —</text>
    </svg>
    <p class="concept-caption">DESIGN 2</p>
  </section>

  <section class="concept concept--three">
    <div class="neck-tag-slot">
      <svg class="neck-tag" width="72" height="80" viewBox="0 0 72 80">
        <path d="M0 0 H72 V64 L36 78 L0 64 Z" fill="url(#copper-foil)"/>
        <text class="vintage" x="36" y="44" text-anchor="middle" font-size="17">2020</text>
      </svg>
    </div>
    <svg class="body-label" width="200" height="180" viewBox="0 0 200 180">
      <rect width="200" height="180" fill="url(#kraft-paper)"/>
      <rect x="8" y="14" width="184" height="156" fill="none" stroke="var(--stitch)" stroke-width="0.8" stroke-dasharray="3 3"/>
      <text class="brand-name" x="100" y="40" text-anchor="middle" font-size="18" style="fill:#2a2018"><tspan x="100">Marlow</tspan><tspan x="100" dy="19">Lane</tspan></text>
      <text class="origin origin--red" x="100" y="164" text-anchor="middle">— •• — NEW ZEALAND — •• —</text>
    </svg>
    <p class="concept-caption">DESIGN 3</p>
  </section>

  <section class="concept concept--four">
    <div class="neck-tag-slot">
      <svg class="neck-tag" width="100" height="92" viewBox="0 0 100 92">
        <path d="M14 14 Q30 2 50 2 Q70 2 86 14 H92 V24 H100 V68 H92 V78 H86 Q70 90 50 90 Q30 90 14 78 H8 V68 H0 V24 H8 V14 Z" fill="url(#copper-foil)"/>
        <text class="vintage" x="50" y="55" text-anchor="middle" font-size="22">2020</text>
      </svg>
    </div>
    <svg class="body-label" width="200" height="190" viewBox="0 0 200 190">
      <path d="M34 24 Q100 -6 166 24 H178 Q178 42 196 44 V146 Q178 148 178 166 H166 Q100 196 34 166 H22 Q22 148 4 146 V44 Q22 42 22 24 Z" fill="var(--cream)" stroke="var(--copper-line)" stroke-width="2"/>
      <text class="brand-name" x="100" y="36" text-anchor="middle" font-size="18"><tspan x="100">Marlow</tspan><tspan x="100" dy="19">Lane</tspan></text>
      <text class="origin origin--dark" x="100" y="172" text-anchor="middle">• NEW ZEALAND •</text>
    </svg>
    <p class="concept-caption">DESIGN 4</p>
  </section>

  <section class="concept concept--five">
    <div class="neck-tag-slot"></div>
    <svg class="body-label" width="200" height="188" viewBox="0 0 200 188">
      <path d="M0 0 H200 V172 L100 186 L0 172 Z" fill="url(#brushed-paper)"/>
      <path d="M10 10 H190 V164 L100 177 L10 164 Z" fill="none" stroke="var(--gold)" stroke-width="1"/>
      <text class="brand-name" x="100" y="40" text-anchor="middle" font-size="18"><tspan x="100">Marlow</tspan><tspan x="100" dy="19">Lane</tspan></text>
      <text class="origin origin--red" x="100" y="158" text-anchor="middle">— •• — NEW ZEALAND — •• —</text>
    </svg>
    <p class="concept-caption">DESIGN 5</p>
  </section>

</main>
</body>
</html>
```